Personal Development Business needs a Business Card Design Project

We need a buiness card design for a new Personal Development business based in S. NSW in Australia called "Willow Path Onward. Our target market is to women who are looking to re-enter the workforce, or already be in the workforce at the middle management level. As a result of consultations their outcomes will be, but not exclusive to: increased confidence, increased self esteem and self awareness, work-life balance, time management, positive thinking.
Behind the scenes of coaching and mentoring will be a spiritual "bent".
Anticipate a beautiful candle as a possible background - showing success and shining - see attachment which came off Pixelmarket. Colours - Unsure until I see something that "grabs my attention". Not esoteric fluffy design but something that suggests safe, professional, supportive of personal journey without being too corporate.
Look forward to what you come up with.
Target Market(s)
Some designers have been requesting various bits of information.
Personal information. See attachment.
Two-sided please.
Gold lines at all four edges.
Many thanks
Ruth
Industry/Entity Type
Business
Look and feel
Each slider illustrates characteristics of the customer's brand and the style your logo design should communicate.

```html
<!DOCTYPE html>
<html lang="en">
<head>
<meta charset="utf-8">
<title>Willow Path Onward – Business Card</title>
<link rel="stylesheet" href="https://fonts.googleapis.com/css2?family=Questrial&family=Roboto:ital,wght@1,700&family=Tinos&display=swap">
<style>
  :root {
    --charcoal: #2c2a2a;
    --night: #0e0c0c;
    --night-warm: #1a1412;
    --paper: #ffffff;
    --ink: #1e1e1e;
    --muted: #3a3a3a;
    --accent-red: #e8192c;
    --gold-dark: #c9a227;
    --gold-mid: #e3c24a;
    --gold-light: #fbf3cf;
    --band: #231f20;
  }
  html, body {
    margin: 0;
    padding: 0;
    width: 1200px;
    height: 416px;
    overflow: hidden;
    background: var(--paper);
  }
  .sheet {
    position: relative;
    width: 1200px;
    height: 416px;
  }
  .card {
    position: absolute;
    top: 0;
    height: 416px;
    overflow: hidden;
  }
  .gold-frame {
    position: absolute;
    box-sizing: border-box;
    border: 5px solid var(--gold-dark);
    border-image: linear-gradient(90deg, var(--gold-dark), var(--gold-mid) 40%, var(--gold-light) 70%, var(--gold-dark)) 1;
    z-index: 3;
  }

  /* Front */
  .card-front {
    left: 0;
    width: 600px;
    background: var(--charcoal);
  }
  .card-front .gold-frame {
    left: 10px; top: 8px; width: 576px; height: 400px;
  }
  .photo-area {
    position: absolute;
    left: 0; top: 228px;
    width: 600px; height: 188px;
    background: linear-gradient(180deg, var(--night), var(--night-warm));
  }
  .brand-title {
    position: absolute;
    left: 0; width: 590px;
    top: 110px;
    margin: 0;
    text-align: center;
    font-family: "Questrial", sans-serif;
    font-weight: 400;
    font-size: 45px;
    letter-spacing: 0.5px;
    color: var(--paper);
  }
  .service-bar {
    position: absolute;
    left: 50px; top: 195px;
    width: 506px; height: 38px;
    background: linear-gradient(90deg, #4a4a4a, #bdbdbd 12%, #f7f7f7 45%, #ffffff 55%, #cfcfcf 85%, #555 100%);
    z-index: 2;
  }
  .service-bar span {
    display: block;
    text-align: center;
    padding-right: 12px;
    font-family: "Tinos", serif;
    font-size: 29px;
    line-height: 38px;
    color: var(--accent-red);
  }

  /* Back */
  .card-back {
    left: 600px;
    width: 600px;
    background: var(--paper);
  }
  .card-back .gold-frame {
    left: 20px; top: 8px; width: 576px; height: 400px;
  }
  .contact-band {
    position: absolute;
    left: 0; top: 228px;
    width: 600px; height: 115px;
    background: var(--band);
  }
  .person-name {
    position: absolute;
    left: 75px; top: 52px;
    margin: 0;
    font-family: "Roboto", sans-serif;
    font-style: italic;
    font-weight: 700;
    font-size: 27px;
    color: var(--ink);
  }
  .credentials {
    position: absolute;
    left: 75px; top: 88px;
    margin: 0; padding: 0;
    list-style: none;
    font-family: "Tinos", serif;
    font-size: 23px;
    line-height: 31px;
    color: var(--ink);
  }
  .contact-list {
    position: absolute;
    left: 67px; top: 232px;
    margin: 0; padding: 0;
    list-style: none;
    font-family: "Tinos", serif;
    font-size: 23px;
    line-height: 31px;
    color: var(--paper);
    z-index: 2;
  }
  .outcomes {
    position: absolute;
    left: 113px;
    top: 362px;
    margin: 0;
    display: flex;
    gap: 26px;
    font-family: "Tinos", serif;
    font-size: 16px;
    color: var(--muted);
  }
</style>
</head>
<body>
<main class="sheet">
  <section class="card card-front">
    <div class="photo-area" role="img" aria-label="Photo of a hand raising a lit candle against a night sky"></div>
    <h1 class="brand-title">Willow Path Onward</h1>
    <div class="service-bar"><span>Personal Development</span></div>
    <div class="gold-frame"></div>
  </section>

  <section class="card card-back">
    <div class="contact-band"></div>
    <h2 class="person-name">Ruth Hallam</h2>
    <ul class="credentials">
      <li>Grad Dip (Mgt) RVU</li>
      <li>BA American History (CVU)</li>
      <li>Master NLP</li>
    </ul>
    <ul class="contact-list">
      <li>Website:&nbsp; willowpathonward.com.au</li>
      <li>Mobile:&nbsp; 0412 555 018</li>
      <li>Email:&nbsp; ruthatwillow@vinetrail.com.au</li>
    </ul>
    <p class="outcomes">
      <span>Self Awareness</span>
      <span>Confidence</span>
      <span>Work-Life Balance</span>
    </p>
    <div class="gold-frame"></div>
  </section>
</main>
</body>
</html>
```